Card for invoking rights with police

Our criminal defense law firm is seeking proposals for a design for our card intended for clients to carry with them in their car. Upon being pulled over, they would hand this card to the officer.
Text for the back of the card:
"For Law Enforcement:"
"I will comply with lawful orders but respectfully decline any test or other requests without my attorney. I wish to remain silent, do not consent to searches, and request to speak with my attorney now.
The back of the card should prominently feature the text and the firm logo should be secondary.
Front
Must prominently feature contact info: 503-555-0182. Do not include attorney name, email, phone from the example file. This is intended to be generic for the firm and not tied to an individual lawyer.
Included for design reference: current business card, firm logo.
We intend to use trenvo.com to produce the cards.
Updates
The back of the card should prominently display the text regarding invocation of rights. Please title it "For Law Enforcement".
Target Market(s)
People who have been stopped by police
Contact Information for Business Card
see project description
Look and feel

```html
<!DOCTYPE html>
<html lang="en">
<head>
<meta charset="utf-8">
<title>Halvorsen Law Firm – Rights Card</title>
<link rel="stylesheet" href="https://fonts.googleapis.com/css2?family=Montserrat:wght@400;500;700&display=swap">
<style>
  :root {
    --bg: #dcdddf;
    --paper: #f2f1ee;
    --navy: #0d3558;
    --grey: #8b8b8b;
    --shadow: rgba(0, 0, 0, 0.16);
  }
  * { box-sizing: border-box; margin: 0; padding: 0; }
  html, body {
    width: 1200px;
    height: 1051px;
    overflow: hidden;
    background: var(--bg);
    font-family: "Montserrat", Arial, sans-serif;
  }
  .canvas {
    width: 1200px;
    height: 1051px;
    display: flex;
    flex-direction: column;
    align-items: center;
    justify-content: center;
    gap: 60px;
  }
  .card {
    width: 620px;
    height: 354px;
    background: var(--paper);
    border-bottom: 4px solid var(--navy);
    box-shadow: 0 14px 30px var(--shadow);
    position: relative;
    display: flex;
    flex-direction: column;
    align-items: center;
  }
  .firm-mark {
    display: flex;
    align-items: center;
    gap: 14px;
    color: var(--navy);
    font-weight: 500;
    letter-spacing: 0.22em;
    text-transform: uppercase;
  }
  .firm-mark .mark-square {
    background: var(--navy);
    flex-shrink: 0;
  }
  /* Front */
  .card--front .firm-mark {
    margin-top: 78px;
    font-size: 30px;
  }
  .card--front .mark-square { width: 40px; height: 40px; }
  .contact {
    margin-top: 62px;
    display: flex;
    align-items: stretch;
    gap: 26px;
  }
  .address {
    text-align: right;
    color: var(--grey);
    font-size: 15px;
    line-height: 1.55;
  }
  .divider {
    width: 1.5px;
    background: var(--navy);
  }
  .channels {
    list-style: none;
    display: flex;
    flex-direction: column;
    justify-content: center;
    gap: 6px;
    color: var(--grey);
    font-size: 15px;
  }
  .channels li { display: flex; align-items: center; gap: 10px; }
  .channels svg { width: 14px; height: 14px; fill: var(--navy); flex-shrink: 0; }
  .channels .phone-main {
    color: var(--navy);
    font-weight: 700;
    font-size: 22px;
    letter-spacing: 0.02em;
  }
  /* Back */
  .card--back .firm-mark {
    margin-top: 48px;
    font-size: 20px;
  }
  .card--back .mark-square { width: 28px; height: 28px; }
  .rights-title {
    margin-top: 36px;
    color: var(--navy);
    font-weight: 700;
    font-size: 22px;
    text-transform: uppercase;
    letter-spacing: 0.01em;
  }
  .rights-text {
    margin-top: 12px;
    width: 540px;
    text-align: center;
    color: var(--grey);
    font-size: 14.5px;
    line-height: 1.5;
  }
</style>
</head>
<body>
<main class="canvas">
  <section class="card card--front" aria-label="Card front">
    <div class="firm-mark">
      <span class="mark-square"></span>
      <span class="firm-name">Halvorsen Law Firm</span>
    </div>
    <div class="contact">
      <address class="address">
        2150 Harbor Ridge Ave NE<br>
        Suite 210<br>
        Lakemont, WA 98040
      </address>
      <span class="divider"></span>
      <ul class="channels">
        <li class="phone-main">
          <svg viewBox="0 0 24 24" aria-hidden="true"><path d="M6.6 10.8a15.1 15.1 0 0 0 6.6 6.6l2.2-2.2a1 1 0 0 1 1-.25 11.4 11.4 0 0 0 3.6.57 1 1 0 0 1 1 1V20a1 1 0 0 1-1 1A17 17 0 0 1 3 4a1 1 0 0 1 1-1h3.5a1 1 0 0 1 1 1c0 1.25.2 2.45.57 3.6a1 1 0 0 1-.25 1z"/></svg>
          503-555-0182
        </li>
        <li>
          <svg viewBox="0 0 24 24" aria-hidden="true"><path d="M7 3h10v4H7zM4 8h16a2 2 0 0 1 2 2v6h-4v5H6v-5H2v-6a2 2 0 0 1 2-2zm4 8v3h8v-3z"/></svg>
          503-555-0147
        </li>
        <li>
          <svg viewBox="0 0 24 24" aria-hidden="true"><path d="M12 2a10 10 0 1 0 0 20 10 10 0 0 0 0-20zm6.9 6h-3a15 15 0 0 0-1.3-4A8 8 0 0 1 18.9 8zM12 4c.8 1.2 1.5 2.5 1.9 4h-3.8c.4-1.5 1.1-2.8 1.9-4zM4.3 14a8 8 0 0 1 0-4h3.4a16 16 0 0 0 0 4zm.8 2h3a15 15 0 0 0 1.3 4A8 8 0 0 1 5.1 16zm3-8h-3a8 8 0 0 1 4.3-4 15 15 0 0 0-1.3 4zM12 20c-.8-1.2-1.5-2.5-1.9-4h3.8c-.4 1.5-1.1 2.8-1.9 4zm2.3-6H9.7a14 14 0 0 1 0-4h4.6a14 14 0 0 1 0 4zm.3 6a15 15 0 0 0 1.3-4h3a8 8 0 0 1-4.3 4zm1.7-6a16 16 0 0 0 0-4h3.4a8 8 0 0 1 0 4z"/></svg>
          www.halvorsenlawfirm.com
        </li>
      </ul>
    </div>
  </section>

  <section class="card card--back" aria-label="Card back">
    <div class="firm-mark">
      <span class="mark-square"></span>
      <span class="firm-name">Halvorsen Law Firm</span>
    </div>
    <h1 class="rights-title">For Law Enforcement:</h1>
    <p class="rights-text">
      I will comply with lawful orders but respectfully decline any test or
      other requests without my attorney. I wish to remain silent, do not
      consent to searches, and request to speak with my attorney now.
    </p>
  </section>
</main>
</body>
</html>
```